Trevalmo New Apparel Company www.trevalmo-wear.com

New Apparel brand, trevalmo has been in business for 2 years and has sales via online, in person and via social media. Looking for a redesign of our current site using existing photographs and images and enhance our ecommerce presentation. We are a squarespace site. currently at www.trevalmo-wear.com and would like to hire a squarespace expert to revise the site and ensure easy integration with tiktok & instagram

Target Market(s)

16-35 year old

Industry/Entity Type

Apparel youth

Coding

Coded - Design and coding required

Number of Pages Required

5+ page

Font styles to use
Sans Serif
Other font styles liked:
• our logo is in Mika and Bimbo

Requirements
Must have
• Squarespace design and sales integration
Nice to have
• Clean modern highlighting the clothes.

```html
<!DOCTYPE html>
<html lang="en">
<head>
<meta charset="utf-8">
<title>Trevalmo — Home</title>
<link rel="stylesheet" href="https://fonts.googleapis.com/css2?family=Poppins:wght@400;500;600;700;800&display=swap">
<style>
  :root {
    --gold: #c9a24a;
    --gold-dark: #b08a35;
    --ink: #111111;
    --black: #0b0b0b;
    --white: #ffffff;
    --grey: #6d6d6d;
    --light: #f1efea;
    --brown: #4a3220;
    --font: "Poppins", Arial, sans-serif;
  }
  * { box-sizing: border-box; margin: 0; padding: 0; }
  html, body { width: 1200px; height: 2596px; overflow: hidden; }
  body { font-family: var(--font); color: var(--ink); background: var(--white); }

  .site-header { height: 84px; display: flex; align-items: center; justify-content: space-between; padding: 0 48px; border-bottom: 1px solid #eee; }
  .brand { font-weight: 800; font-size: 30px; color: var(--gold); letter-spacing: .5px; }
  .main-nav { display: flex; gap: 34px; font-size: 15px; font-weight: 500; }
  .header-actions { display: flex; align-items: center; gap: 18px; }
  .login-btn { border: 1px solid var(--ink); padding: 6px 18px; font-size: 13px; border-radius: 3px; }
  .icon { width: 20px; height: 20px; }

  .hero { height: 380px; background: var(--black); display: flex; position: relative; overflow: hidden; }
  .hero-photo { width: 56%; height: 100%; background: linear-gradient(135deg, #6f7479 0%, #b9bcbf 45%, #3b3e41 100%); }
  .hero-copy { padding: 100px 0 0 60px; color: var(--white); position: relative; z-index: 1; }
  .hero-copy h1 { font-size: 44px; font-weight: 500; line-height: 1.15; }
  .btn-gold { display: inline-block; background: var(--gold); color: var(--white); font-size: 14px; font-weight: 500; padding: 10px 28px; border-radius: 2px; }
  .hero-copy .btn-gold { margin-top: 24px; }
  .hero-mark { position: absolute; bottom: -40px; left: 380px; font-size: 150px; font-weight: 800; color: #1c1c1c; letter-spacing: 4px; }

  .gallery { padding: 22px 40px 0; display: grid; grid-template-columns: repeat(3, 1fr); grid-template-rows: 220px 230px; gap: 12px; }
  .tile { border-radius: 2px; }
  .tile-navy { background: linear-gradient(160deg, #0f1b3a, #1d2f5e 60%, #0a1124); }
  .tile-sunset { grid-row: span 2; background: linear-gradient(180deg, #f1b35c 0%, #c98a4c 30%, #6d6b63 60%, #3a3a36 100%); }
  .tile-car { background: linear-gradient(150deg, #d7d3cc, #9b958c 55%, #3f3c38); }
  .tile-wall { background: linear-gradient(135deg, #ff4f8b, #7b3fe4 40%, #2fc2e6 70%, #f6c341); }
  .story-card { background: var(--brown); color: var(--white); padding: 34px 34px; }
  .story-card h2 { font-size: 24px; font-weight: 600; margin-bottom: 12px; }
  .story-card p { font-size: 13px; line-height: 1.6; color: #e7dccf; margin-bottom: 20px; }
  .pager { display: flex; justify-content: flex-end; gap: 8px; padding: 14px 40px 22px; }
  .pager span { width: 30px; height: 30px; border: 1px solid #ccc; display: flex; align-items: center; justify-content: center; }
  .pager .active { background: var(--gold); border-color: var(--gold); }

  .best-sellers { background: var(--gold); height: 470px; padding: 42px 70px 0; position: relative; }
  .best-sellers h2 { text-align: center; color: var(--white); font-size: 36px; font-weight: 500; margin-bottom: 34px; }
  .products { display: grid; grid-template-columns: repeat(4, 1fr); gap: 26px; }
  .product { background: var(--white); padding: 16px 16px 20px; position: relative; text-align: center; }
  .product-img { height: 190px; margin-bottom: 14px; }
  .product h3 { font-size: 13px; font-weight: 500; line-height: 1.4; height: 38px; }
  .product .btn-gold { margin-top: 12px; font-size: 12px; padding: 8px 20px; }
  .badge { position: absolute; top: 12px; left: 12px; background: var(--ink); color: var(--white); font-size: 11px; padding: 2px 10px; }
  .img-shorts { background: linear-gradient(180deg, #eceae4, #c9b79a); }
  .img-hoodie { background: linear-gradient(180deg, #eceae4, #1d1d1d); }
  .img-sleeve { background: linear-gradient(180deg, #eceae4, #262626); }
  .img-sweater { background: linear-gradient(180deg, #eceae4, #d9d0c2); }
  .best-sellers .pager { position: absolute; right: 70px; bottom: 18px; padding: 0; }
  .best-sellers .pager span { border-color: var(--white); }
  .best-sellers .pager .active { background: var(--white); }

  .tagline { height: 200px; display: flex; align-items: center; justify-content: center; text-align: center; }
  .tagline h2 { font-size: 38px; font-weight: 500; line-height: 1.3; }

  .collage { padding: 0 110px; display: grid; grid-template-columns: 1fr 1fr 1fr; grid-template-rows: 330px 240px; gap: 12px; height: 582px; }
  .c-beige { background: linear-gradient(160deg, #d8cdb8, #9c8f7a); }
  .c-green { background: linear-gradient(160deg, #7e8b5b, #4b5a36); }
  .c-black { background: linear-gradient(160deg, #3a3a3a, #0d0d0d); }
  .c-field { background: linear-gradient(180deg, #bcd3e6, #8da96a 60%, #5b7b3d); }
  .c-brick { grid-row: span 2; background: linear-gradient(160deg, #a0563d, #6d3a2b 60%, #3b2219); }

  .site-footer { margin-top: 40px; background: var(--black); color: var(--white); height: 310px; padding: 44px 70px 0; }
  .signup { display: flex; align-items: center; gap: 30px; justify-content: center; }
  .signup h3 { font-size: 20px; font-weight: 500; line-height: 1.3; width: 260px; }
  .signup-field { width: 320px; height: 40px; background: var(--white); color: #999; font-size: 13px; padding: 10px 14px; }
  .footer-main { display: flex; justify-content: space-between; align-items: flex-end; margin-top: 56px; }
  .footer-brand { font-size: 52px; font-weight: 800; color: var(--white); }
  .footer-links { display: flex; gap: 20px; font-size: 13px; color: #ccc; }
  .socials { display: flex; gap: 12px; justify-content: flex-end; margin-top: 14px; }
  .socials span { width: 22px; height: 22px; border-radius: 50%; background: var(--white); display: block; }
  .copyright { border-top: 1px solid #2a2a2a; margin-top: 26px; padding-top: 14px; text-align: center; font-size: 12px; color: #999; }
</style>
</head>
<body>
  <header class="site-header">
    <div class="brand">trevalmo</div>
    <nav class="main-nav"><span>Home</span><span>Shop</span><span>About</span><span>Contact</span></nav>
    <div class="header-actions">
      <span class="login-btn">Login</span>
      <svg class="icon" viewBox="0 0 24 24" fill="none" stroke="#111" stroke-width="2"><circle cx="11" cy="11" r="7"/><path d="M16 16l5 5"/></svg>
      <svg class="icon" viewBox="0 0 24 24" fill="none" stroke="#111" stroke-width="2"><circle cx="12" cy="8" r="4"/><path d="M4 21c1-5 15-5 16 0"/></svg>
      <svg class="icon" viewBox="0 0 24 24" fill="none" stroke="#111" stroke-width="2"><path d="M5 8h14l-1 13H6z"/><path d="M9 8a3 3 0 016 0"/></svg>
    </div>
  </header>

  <section class="hero">
    <div class="hero-photo" role="img" aria-label="Sprinter in a white vest racing down a track"></div>
    <div class="hero-copy">
      <h1>Introducing<br>Success</h1>
      <span class="btn-gold">Shop Now</span>
    </div>
    <div class="hero-mark" aria-hidden="true">trevalmo</div>
  </section>

  <section class="gallery">
    <div class="tile tile-navy" role="img" aria-label="Navy garment with embroidered brand name"></div>
    <div class="tile tile-sunset" role="img" aria-label="Model in a black tracksuit leaning on a car at sunset"></div>
    <div class="tile tile-car" role="img" aria-label="Printed tee laid across a car bonnet"></div>
    <div class="tile story-card">
      <h2>Trevalmo</h2>
      <p>Handmade streetwear for a new generation, built to stand out and made to last.</p>
      <span class="btn-gold">Shop Now</span>
    </div>
    <div class="tile tile-wall" role="img" aria-label="Model in a pink hoodie before a colourful mural"></div>
  </section>
  <div class="pager">
    <span><svg width="12" height="12" viewBox="0 0 12 12"><path d="M8 1L3 6l5 5" fill="none" stroke="#111" stroke-width="1.6"/></svg></span>
    <span class="active"><svg width="12" height="12" viewBox="0 0 12 12"><path d="M4 1l5 5-5 5" fill="none" stroke="#fff" stroke-width="1.6"/></svg></span>
  </div>

  <section class="best-sellers">
    <h2>Best Selling Products</h2>
    <div class="products">
      <article class="product">
        <div class="product-img img-shorts" role="img" aria-label="Sand tee and shorts set"></div>
        <h3>Sand Tee and Shorts</h3>
        <span class="btn-gold">Add to cart</span>
      </article>
      <article class="product">
        <span class="badge">Hot</span>
        <div class="product-img img-hoodie" role="img" aria-label="Black hoodie"></div>
        <h3>Trevalmo Black Hoodie</h3>
        <span class="btn-gold">Add to cart</span>
      </article>
      <article class="product">
        <div class="product-img img-sleeve" role="img" aria-label="Black long sleeve shirt"></div>
        <h3>Long Sleeve Shirt Collection</h3>
        <span class="btn-gold">Add to cart</span>
      </article>
      <article class="product">
        <div class="product-img img-sweater" role="img" aria-label="Cream shoulder sweater"></div>
        <h3>Shoulder Sweater Collection</h3>
        <span class="btn-gold">Add to cart</span>
      </article>
    </div>
    <div class="pager">
      <span><svg width="12" height="12" viewBox="0 0 12 12"><path d="M8 1L3 6l5 5" fill="none" stroke="#fff" stroke-width="1.6"/></svg></span>
      <span class="active"><svg width="12" height="12" viewBox="0 0 12 12"><path d="M4 1l5 5-5 5" fill="none" stroke="#c9a24a" stroke-width="1.6"/></svg></span>
    </div>
  </section>

  <section class="tagline">
    <h2>Each is made by hand with a unique<br>design and feel.</h2>
  </section>

  <section class="collage">
    <div class="c-beige" role="img" aria-label="Model in a beige hoodie"></div>
    <div class="c-black" role="img" aria-label="Model in a black tee outdoors"></div>
    <div class="c-brick" role="img" aria-label="Model in a hoodie against a brick wall"></div>
    <div class="c-green" role="img" aria-label="Olive hoodie with brand name print"></div>
    <div class="c-field" role="img" aria-label="Group playing football on a field"></div>
  </section>

  <footer class="site-footer">
    <div class="signup">
      <h3>Sign up to Receive News and Updates.</h3>
      <div class="signup-field">Email address</div>
      <span class="btn-gold">Sign Up</span>
    </div>
    <div class="footer-main">
      <div class="footer-brand">trevalmo</div>
      <div>
        <div class="footer-links"><span>Shipping &amp; Returns</span><span>Size Guide</span><span>FAQs</span><span>Terms</span><span>Privacy Policy</span></div>
        <div class="socials"><span></span><span></span><span></span></div>
      </div>
    </div>
    <div class="copyright">© 2024 Trevalmo. All rights reserved.</div>
  </footer>
</body>
</html>
```